New homepage concept needed for online reading programs website

About the Academy of Literacy Growth:
The Institute teaches online summer reading skills programs for entering fourth graders, offered through partnerships with universities, colleges, and municipalities nationwide. The goal of the program is to build reading skills (long-word decoding, fluency and comprehension), and foster a lifelong love of books and reading.

Aims & Target Market:
The Institute has developed a new format of its online reading program for fourth graders, which includes live small-group video classes taught by a professional reading teacher. The Institute seeks a mock-up of a homepage of the website used to market this new program. The primary audience for this website is the parents of these 4th graders. Traffic to this website is driven by direct-marketing campaigns directed at parents and students.

Live classes for children are completely new in online education, unlike anything else in the marketplace, and parents therefor have no experience with them. The successful homepage mock-up will include illustrations or photographs that allow visitors to immediately grasp/understand the new format, without relying on a written description. Additionally, the successful homepage concept will make the program, and the video classes in particular, feel fun and appealing to kids and parents alike.

There are three main elements to the program, and each needs to be represented graphically on the homepage, with particular emphasis on the small-group video classes:
1. Live small-group video classes (weekly for six weeks):
a. During video class discussions, the student’s computer (or tablet) screen is filled with live video frames of the teacher and the other students. The video frame for the teacher is larger, and the other students appear in smaller frames.
b. During other video class instruction, the teacher uses a presentation screen to display pages of a book or a “whiteboard” used for instructional activities.
c. The homepage mock-up could include a screenshot of the video classes themselves, with children looking engaged and a teacher leading them in discussion. We have included a screen shot of one of these classes for reference, but do not feel constrained to represent this screen realistically (as shown here). It can be changed around – teacher in the center, etc.). Alternately, if there is a graphic other than a screen shot that you feel could be used to bring across the concept of the video classes, feel free.
2. Individualized online instruction
a. Graphics could include screenshots of the video lessons students complete in between these weekly classes and/or images of a child or children at computer(s).
3. Independent reading in great books
a. Graphics could include some or all of the program books, which can be pulled from our current website (link below), and/or images of a child or children reading.

An example of our current online program website can be seen at http://fenwick.webliteracystudio.example/4/Home. Please reference this site for information on program goals, books/materials, and site navigation.
The successful design will be welcoming and inviting, and allow parents and students to immediately grasp what the programs are, with particular emphasis on the live small-group video classes.

Copy and Specifications:
Sample copy has been provided for reference, as well as a screen shot of our sample classes to show what students will see on screen. Also included are stills of our online video lessons to illustrate the online instruction aspect.

```html
<!DOCTYPE html>
<html lang="en">
<head>
<meta charset="utf-8">
<title>Reading Skills – Online Program for 4th and 5th Graders</title>
<link href="https://fonts.googleapis.com/css2?family=Ubuntu:wght@400;500&family=Open+Sans:wght@400;600&family=Roboto:wght@700&display=swap" rel="stylesheet">
<style>
:root{
  --blue:#1b63a6;
  --blue-light:#5fb0e3;
  --orange:#f47a1f;
  --green:#22a64a;
  --green-link:#1e8a3c;
  --text:#555;
  --heading:#4a4a4a;
  --hero-bg:#efefef;
  --benefit-bg:#f5f6f7;
  --footer-bg:#2a2a2b;
  --footer-text:#a9a9a9;
  --badge:#174d2a;
}
*{margin:0;padding:0;box-sizing:border-box}
html,body{width:886px;height:1200px;overflow:hidden;background:#fff;font-family:"Ubuntu",sans-serif;color:var(--text)}
.page{position:relative;width:886px;height:1200px}
.header{position:absolute;top:0;left:0;width:886px;height:77px}
.brand{position:absolute;left:97px;top:17px}
.brand-name{font-family:"Open Sans",sans-serif;font-weight:600;font-size:24px;color:var(--blue);letter-spacing:-.3px;line-height:1}
.brand-tag{font-family:"Roboto",sans-serif;font-weight:700;font-size:11px;color:var(--orange);margin-top:6px}
.call{position:absolute;left:655px;top:24px;display:flex;align-items:center;gap:10px}
.call-label{font-size:10px;color:#444}
.call-number{font-size:15px;color:var(--orange);font-weight:500;margin-top:2px}
.nav{position:absolute;top:77px;left:0;width:886px;height:40px;background:var(--blue);display:flex;padding-left:96px}
.nav a{color:#fff;text-decoration:none;font-size:11px;line-height:40px;padding:0 10.5px}
.nav a.active{background:var(--blue-light);color:#1d3f5e;padding:0 16px}
.hero{position:absolute;top:117px;left:0;width:886px;height:293px;background:var(--hero-bg)}
.hero-video{position:absolute;left:96px;top:31px;width:340px;height:213px;border:4px solid #dcdcdc;background:linear-gradient(135deg,#2a86e6,#1c66d0)}
.play{position:absolute;left:138px;top:84px}
.dots{position:absolute;left:240px;top:260px;display:flex;gap:6px}
.dots span{width:9px;height:9px;border-radius:50%;background:#d3d3d3}
.dots span.on{background:var(--blue)}
.hero-copy{position:absolute;left:471px;top:36px;width:320px}
.hero-title{font-family:"Open Sans",sans-serif;font-weight:600;font-size:24px;line-height:31px;color:var(--heading)}
.hero-title em{font-style:normal;color:var(--orange)}
.hero-text{font-size:10px;line-height:17.6px;margin-top:14px;color:#666}
.btn{position:absolute;left:1px;top:144px;width:133px;height:40px;background:var(--green);border-bottom:3px solid #178238;color:#fff;font-size:13px;display:flex;align-items:center;text-decoration:none}
.btn-icon{width:32px;height:100%;display:flex;align-items:center;justify-content:center;border-right:1px solid #1c913f}
.btn span{padding-left:10px}
.features{position:absolute;top:459px;left:97px;display:flex;gap:24px}
.feature{width:215px;text-align:center}
.feature-img{width:215px;height:118px}
.feature h3{font-family:"Open Sans",sans-serif;font-weight:600;font-size:14px;line-height:19px;color:var(--orange);margin-top:17px}
.feature p{font-size:10px;line-height:15px;margin-top:9px;color:#666}
.feature a{display:block;font-size:10px;font-style:italic;color:var(--green-link);text-decoration:none;margin-top:4px}
.benefits{position:absolute;top:730px;left:0;width:886px;height:282px;background:var(--benefit-bg)}
.benefits-img{position:absolute;left:520px;top:24px;width:280px;height:230px;border-radius:40%;background:radial-gradient(ellipse at 60% 45%,#d8c7b2 0%,#e9e4dd 40%,rgba(245,246,247,0) 72%)}
.benefits h2{position:absolute;left:98px;top:35px;width:400px;font-weight:400;font-size:12.5px;line-height:18px;color:var(--blue)}
.benefit-list{position:absolute;left:98px;top:92px;list-style:none;width:200px}
.benefit-list li{font-size:10.5px;line-height:23px;border-bottom:1px solid #e0e0e0;padding-left:24px;position:relative;color:#555}
.benefit-list li::before{content:"→";position:absolute;left:5px;color:var(--orange);font-size:11px;font-weight:500}
.benefits-note{position:absolute;left:98px;top:200px;width:480px;font-size:9.7px;line-height:17.6px;color:#666}
.footer{position:absolute;top:1012px;left:0;width:886px;height:188px;background:var(--footer-bg)}
.copyright{position:absolute;left:98px;top:31px;font-size:10px;line-height:19px;color:var(--footer-text)}
.follow{position:absolute;left:410px;top:27px}
.follow-label{font-size:11px;color:var(--footer-text)}
.social{display:flex;gap:4px;margin-top:12px}
.social a{width:22px;height:22px;border-radius:50%;background:#fff;display:flex;align-items:center;justify-content:center}
.partner{position:absolute;left:647px;top:34px;width:143px;height:38px;background:var(--badge);border:2px solid #7e7e7e;display:flex;align-items:center;justify-content:center;gap:8px}
.partner-mark{width:14px;height:18px;background:#e8c531}
.partner-name{font-family:"Open Sans",sans-serif;font-size:18px;color:#fff}
.footer-rule{position:absolute;left:96px;top:93px;width:694px;height:1px;background:#444}
.footer-note{position:absolute;left:96px;top:117px;width:694px;text-align:center;font-size:9px;line-height:17.6px;color:#7c7c7c}
</style>
</head>
<body>
<div class="page">
  <header class="header">
    <div class="brand">
      <div class="brand-name">Reading Skills</div>
      <div class="brand-tag">Online Program for 4th and 5th Graders</div>
    </div>
    <div class="call">
      <svg width="29" height="29" viewBox="0 0 29 29" aria-hidden="true"><circle cx="14.5" cy="14.5" r="13.5" fill="none" stroke="#ccc"/><path d="M9 12.5c0-1.5 2.5-2.5 5.5-2.5s5.5 1 5.5 2.5v1h-2.5v-1h-6v1H9z M10.5 14.5h8l1 4h-10z" fill="#bbb"/></svg>
      <div>
        <div class="call-label">Call Us :</div>
        <div class="call-number">1-800-555-0142</div>
      </div>
    </div>
  </header>

  <nav class="nav">
    <a class="active" href="#">Home</a>
    <a href="#">Independent Reading</a>
    <a href="#">Comprehension</a>
    <a href="#">Long-Word Decoding</a>
    <a href="#">Fluency &amp; Speed</a>
    <a href="#">About the Teachers</a>
    <a href="#">FAQ</a>
    <a href="#">Enroll</a>
  </nav>

  <section class="hero">
    <div class="hero-video" role="img" aria-label="Video lesson still: teacher presenting the word 'suddenly' on a blue screen">
      <svg class="play" width="56" height="56" viewBox="0 0 56 56" aria-hidden="true"><circle cx="28" cy="28" r="27" fill="#1f3350" opacity=".9"/><path d="M22 15v26l20-13z" fill="#fff"/></svg>
    </div>
    <div class="dots"><span class="on"></span><span></span><span></span><span></span></div>
    <div class="hero-copy">
      <h1 class="hero-title">Long-Word Decoding<br><em>Video’s</em></h1>
      <p class="hero-text">Sed ut perspiciatis unde omnis iste natus error sit voluptatem accu­santium doloremque laudantium, totam rem aperiam, eaque ipsa quae ab illo inventore sunt explicabo.</p>
      <a class="btn" href="#">
        <div class="btn-icon"><svg width="10" height="11" viewBox="0 0 10 11" aria-hidden="true"><circle cx="5" cy="3" r="2.6" fill="#fff"/><path d="M0 11c0-3 2-5 5-5s5 2 5 5z" fill="#fff"/></svg></div>
        <span>Online Now!</span>
      </a>
    </div>
  </section>

  <section class="features">
    <article class="feature">
      <div class="feature-img" role="img" aria-label="Children gathered around a laptop in a classroom" style="background:linear-gradient(135deg,#c9b79c,#e6d6c2 50%,#b9a58a)"></div>
      <h3>Live small-group video<br>classes</h3>
      <p>Sed ut perspiciatis unde omnis iste natus error sit voluptatem accusantium dolor.</p>
      <a href="#">Read More &gt;&gt;</a>
    </article>
    <article class="feature">
      <div class="feature-img" role="img" aria-label="Boy with glasses working at a laptop beside a stack of books" style="background:linear-gradient(135deg,#d9dfe6,#f1f1f1 55%,#c8c2b8)"></div>
      <h3>Individualized Online<br>Instruction</h3>
      <p>Sed ut perspiciatis unde omnis iste natus error sit voluptatem accusantium dolor.</p>
      <a href="#">Read More &gt;&gt;</a>
    </article>
    <article class="feature">
      <div class="feature-img" role="img" aria-label="Girl resting on an open book between stacks of books" style="background:linear-gradient(135deg,#e8e3dc,#f4efe9 50%,#cdb8a0)"></div>
      <h3>Independent<br>reading in great books</h3>
      <p>Sed ut perspiciatis unde omnis iste natus error sit voluptatem accusantium dolor.</p>
      <a href="#">Read More &gt;&gt;</a>
    </article>
  </section>

  <section class="benefits">
    <div class="benefits-img" role="img" aria-label="Young boy lying on the floor reading an open book"></div>
    <h2>This program will help your child become a skilled enthusiastic reader with strong comprehension. Your child will :</h2>
    <ul class="benefit-list">
      <li>Build long-word decoding skills</li>
      <li>Read more fluently and rapidly</li>
      <li>Improve comprehension</li>
      <li>Become a strong, enthusiastic reader</li>
    </ul>
    <p class="benefits-note">The program includes engaging online instruction, effective materials, and great books, and is customized for your child’s reading level. You will also receive support from a professional reading teacher.</p>
  </section>

  <footer class="footer">
    <div class="copyright">Copyright © 2014 Academy of Literacy Growth<br>I Privacy Policy</div>
    <div class="follow">
      <div class="follow-label">Follow Us</div>
      <div class="social">
        <a href="#" aria-label="Email"><svg width="12" height="9" viewBox="0 0 12 9" aria-hidden="true"><rect x=".5" y=".5" width="11" height="8" fill="none" stroke="#2a2a2b"/><path d="M.5 .5 6 5l5.5-4.5" fill="none" stroke="#2a2a2b"/></svg></a>
        <a href="#" aria-label="Chat"><svg width="12" height="11" viewBox="0 0 12 11" aria-hidden="true"><path d="M1 1h10v6H5l-3 3V7H1z" fill="#2a2a2b"/></svg></a>
        <a href="#" aria-label="Share"><svg width="12" height="12" viewBox="0 0 12 12" aria-hidden="true"><circle cx="9.5" cy="2.5" r="2" fill="#2a2a2b"/><circle cx="2.5" cy="6" r="2" fill="#2a2a2b"/><circle cx="9.5" cy="9.5" r="2" fill="#2a2a2b"/><path d="M9.5 2.5 2.5 6l7 3.5" fill="none" stroke="#2a2a2b"/></svg></a>
        <a href="#" aria-label="Website"><svg width="12" height="12" viewBox="0 0 12 12" aria-hidden="true"><circle cx="6" cy="6" r="5" fill="none" stroke="#2a2a2b"/><ellipse cx="6" cy="6" rx="2.2" ry="5" fill="none" stroke="#2a2a2b"/><path d="M1 6h10" stroke="#2a2a2b"/></svg></a>
        <a href="#" aria-label="Updates"><svg width="11" height="12" viewBox="0 0 11 12" aria-hidden="true"><path d="M5.5 1C3.5 1 2.5 2.5 2.5 4.5V7L1 9h9L8.5 7V4.5C8.5 2.5 7.5 1 5.5 1z" fill="#2a2a2b"/><circle cx="5.5" cy="10.5" r="1.2" fill="#2a2a2b"/></svg></a>
      </div>
    </div>
    <div class="partner"><span class="partner-mark"></span><span class="partner-name">FENWICK</span></div>
    <div class="footer-rule"></div>
    <p class="footer-note">The Summer Reading Program is a program of Fenwick’s Constituent Engagement division operated by an independent, third party organization, the Academy of Literacy Growth. For questions about the program or to register, please contact a program coordinator at (800) 555-0177. For other inquiries, contact Mara Ellison with Fenwick University, (254) 555-0119.</p>
  </footer>
</div>
</body>
</html>
```